Valo T-rekka: Flyer for specialized institutions

✅ Specifications – Creation of an Institutional Flyer – Valo T-rekka
🎯 Main objective
Create a striking, clear and attractive flyer for specialist institutions, to encourage them to organize outings with Valo T-rekka by highlighting:
• Accessibility for people with reduced mobility.
• The adapted Brivex Duolo.
• The unique mountain experience.
• The professionalism and kindness of the team.
________________________________________
🧩 Context
Valo T-rekka offers mountain hikes using an electric Brivex Duolo, specially designed for people with disabilities. The goal is to provide an immersive experience in the great outdoors, even for people with severe mobility limitations.
👥 Target audience
• Managers of medical-social establishments.
• Specialized educators, facilitators, occupational therapists.
• Institutions welcoming people with motor or mental disabilities.
💡 Key message to convey
"With Valo T-rekka, open the doors to the mountains for your guests. Offer them an unforgettable experience in the great outdoors thanks to our specially adapted Brivex Duolo."
📝 Content to integrate
🔹 Main hook (strong visual impact)
“The mountains accessible to all, finally possible!”
🔹 Presentation text
• Short presentation of Valo T-rekka.
• Highlighting the Brivex Duolo:
o Fully adapted.
o Ease of installation.
o Comfort and safety.
• Description of the experience:
o Exceptional panoramas.
o Gentle sensations and total immersion.
o Caring and professional supervision.
🔹 Promise / benefits
• Total inclusivity: accessible even to people with severe disabilities.
• Enriching and rewarding outing for participants.
• Supervision by a passionate, trained and caring team.
🔹 Practical information
• Location / Areas served.
• Duration of outings.
• Capacity (1 person per Brivex + accompanying person).
• Contact (reservation, questions, quotes, etc.).
🔹 Contact details
• Valo T-rekka logo.
• Telephone / Email / Website.
• Social networks (if relevant).
• QR Code to demonstration video or website.

Target Market(s)

Specialized institutions with people with disabilities

Industry/Entity Type

Tourisme, activité en montagne

Font styles to use
Sans Serif

Colors
00AB8E
00BBA5
67D7C9
C6EFE9
E9F9F6

Requirements
Must have
• It's aimed at leaders and should appeal to their sensibilities. You should feel that it's a fun, peaceful, and safe activity.
Nice to have
• A4 format (front / back)
Should not have
• I don't want blurring but I need to change the faces of the people in the photos, I don't have permission to use their faces.

```html
<!DOCTYPE html>
<html lang="en">
<head>
<meta charset="utf-8">
<title>Valo T-rekka – Institutional Flyer</title>
<link href="https://fonts.googleapis.com/css2?family=Anton&family=Montserrat:wght@400;600;700;800&display=swap" rel="stylesheet">
<style>
:root{
  --green:#8cc63f;
  --green-dark:#5e9a22;
  --ink:#1f2326;
  --text:#3a3f44;
  --paper:#ffffff;
  --stage:#e6e8ea;
  --sky-top:#9cc3e0;
  --sky-low:#dfe9ef;
  --meadow:#6f9a4a;
  --rock:#8d8f8a;
}
*{box-sizing:border-box;margin:0;padding:0}
html,body{width:870px;height:1200px;overflow:hidden}
body{background:var(--stage);font-family:'Montserrat',sans-serif;color:var(--text);position:relative}
.page{position:absolute;top:303px;width:420px;height:594px;background:var(--paper);overflow:hidden;box-shadow:0 4px 14px rgba(0,0,0,.18)}
.page--front{left:10px}
.page--back{left:440px}
.photo{position:absolute;background:linear-gradient(180deg,var(--sky-top) 0%,var(--sky-low) 45%,var(--rock) 62%,var(--meadow) 100%)}
.accent{position:absolute}
.brand{position:absolute;top:22px;left:22px;display:flex;align-items:center;gap:6px;font-weight:800;font-size:15px;color:var(--ink);z-index:3}
.brand__dot{width:14px;height:14px;border-radius:50%;background:var(--green)}
.headline{position:absolute;left:22px;top:68px;font-family:'Anton',sans-serif;font-size:28px;line-height:1.05;color:var(--ink);text-transform:uppercase;z-index:3;white-space:nowrap}
.headline em{font-style:normal;color:var(--green)}
.section-title{font-family:'Anton',sans-serif;font-size:17px;color:var(--green);text-transform:uppercase;letter-spacing:.3px;margin-bottom:6px}
.body-text{font-size:8.2px;line-height:1.45}
.ticks{list-style:none}
.ticks li{position:relative;padding-left:13px;font-size:8px;line-height:1.35;margin-bottom:4px}
.ticks li svg{position:absolute;left:0;top:1px;width:9px;height:9px}
.footer{position:absolute;left:0;bottom:0;width:100%;height:26px;background:var(--green);color:#fff;font-weight:700;font-size:9px;display:flex;align-items:center;justify-content:center;gap:14px;letter-spacing:.3px}
.contact-item{display:flex;align-items:center;gap:4px;font-size:8px}
.contact-item svg{width:9px;height:9px}
</style>
</head>
<body>

<section class="page page--front">
  <div class="photo" style="left:200px;top:0;width:220px;height:310px" role="img" aria-label="Photo: participants riding the adapted Brivex Duolo on an alpine trail, faces replaced"></div>
  <svg class="accent" style="left:0;top:0" width="420" height="320" viewBox="0 0 420 320">
    <polygon points="0,0 285,0 205,320 0,320" fill="#ffffff"/>
    <polygon points="285,0 308,0 228,320 205,320" fill="var(--green)"/>
    <polygon points="340,0 420,0 420,55" fill="var(--green)" opacity=".85"/>
  </svg>
  <div class="brand"><span class="brand__dot"></span>Valo T-rekka</div>
  <h1 class="headline">The <em>mountains</em><br>accessible to all,<br><em>finally</em><br><em>possible!</em></h1>

  <div style="position:absolute;left:22px;top:330px;width:376px">
    <h2 class="section-title">Context</h2>
    <p class="body-text">Valo T-rekka offers mountain hikes using an electric Brivex Duolo, specially designed for people with disabilities. The goal is to provide an immersive experience in the great outdoors, even for people with severe mobility limitations.</p>
  </div>

  <div class="photo" style="left:0;top:420px;width:420px;height:148px" role="img" aria-label="Photo: group outing with the Brivex Duolo in a green mountain meadow"></div>
  <svg class="accent" style="left:0;top:418px" width="420" height="30" viewBox="0 0 420 30"><polygon points="0,0 420,0 420,6 0,26" fill="#ffffff"/></svg>

  <div style="position:absolute;left:18px;top:470px;width:384px;display:flex;gap:10px;z-index:2">
    <ul class="ticks" style="flex:1;background:rgba(255,255,255,.92);padding:8px 8px 4px;border-left:3px solid var(--green)">
      <li><svg viewBox="0 0 10 10"><path d="M1 5l3 3 5-6" stroke="var(--green)" stroke-width="2" fill="none"/></svg>Fully adapted</li>
      <li><svg viewBox="0 0 10 10"><path d="M1 5l3 3 5-6" stroke="var(--green)" stroke-width="2" fill="none"/></svg>Ease of installation</li>
      <li><svg viewBox="0 0 10 10"><path d="M1 5l3 3 5-6" stroke="var(--green)" stroke-width="2" fill="none"/></svg>Comfort and safety</li>
    </ul>
    <ul class="ticks" style="flex:1.3;background:rgba(255,255,255,.92);padding:8px 8px 4px;border-left:3px solid var(--green)">
      <li><svg viewBox="0 0 10 10"><path d="M1 5l3 3 5-6" stroke="var(--green)" stroke-width="2" fill="none"/></svg>Exceptional panoramas</li>
      <li><svg viewBox="0 0 10 10"><path d="M1 5l3 3 5-6" stroke="var(--green)" stroke-width="2" fill="none"/></svg>Gentle sensations and total immersion</li>
      <li><svg viewBox="0 0 10 10"><path d="M1 5l3 3 5-6" stroke="var(--green)" stroke-width="2" fill="none"/></svg>Caring and professional supervision</li>
    </ul>
  </div>
  <div class="footer">www.valo-t-rekka.ch</div>
</section>

<section class="page page--back">
  <div class="photo" style="left:250px;top:0;width:170px;height:200px" role="img" aria-label="Photo: passenger and guide aboard the Brivex Duolo, faces replaced"></div>
  <svg class="accent" style="left:0;top:0" width="420" height="210" viewBox="0 0 420 210">
    <polygon points="0,0 280,0 250,200 0,200" fill="#ffffff"/>
    <polygon points="280,0 296,0 266,200 250,200" fill="var(--green)"/>
  </svg>
  <div style="position:absolute;left:22px;top:26px;width:225px">
    <h2 class="section-title">Promise / Benefits</h2>
    <ul class="ticks">
      <li><svg viewBox="0 0 10 10"><path d="M1 5l3 3 5-6" stroke="var(--green)" stroke-width="2" fill="none"/></svg>Total inclusivity: accessible even to people with severe disabilities.</li>
      <li><svg viewBox="0 0 10 10"><path d="M1 5l3 3 5-6" stroke="var(--green)" stroke-width="2" fill="none"/></svg>Enriching and rewarding outing for participants.</li>
      <li><svg viewBox="0 0 10 10"><path d="M1 5l3 3 5-6" stroke="var(--green)" stroke-width="2" fill="none"/></svg>Supervision by a passionate, trained and caring team.</li>
    </ul>
    <p class="body-text" style="margin-top:8px">With Valo T-rekka, open the doors to the mountains for your guests. Offer them an unforgettable experience in the great outdoors thanks to our specially adapted Brivex Duolo.</p>
  </div>

  <div class="photo" style="left:0;top:200px;width:420px;height:130px" role="img" aria-label="Photo: alpine panorama with a Brivex Duolo on a mountain path"></div>
  <div style="position:absolute;left:0;top:326px;width:420px;height:4px;background:var(--green)"></div>

  <div style="position:absolute;left:22px;top:345px;width:376px">
    <h2 class="section-title">Practical information</h2>
    <ul class="ticks">
      <li><svg viewBox="0 0 10 10"><path d="M1 5l3 3 5-6" stroke="var(--green)" stroke-width="2" fill="none"/></svg>Location / Areas served</li>
      <li><svg viewBox="0 0 10 10"><path d="M1 5l3 3 5-6" stroke="var(--green)" stroke-width="2" fill="none"/></svg>Duration of outings</li>
      <li><svg viewBox="0 0 10 10"><path d="M1 5l3 3 5-6" stroke="var(--green)" stroke-width="2" fill="none"/></svg>Capacity (1 person per Brivex + accompanying person)</li>
      <li><svg viewBox="0 0 10 10"><path d="M1 5l3 3 5-6" stroke="var(--green)" stroke-width="2" fill="none"/></svg>Contact (reservation, questions, quotes, etc.)</li>
    </ul>
  </div>

  <div class="photo" style="left:0;top:445px;width:420px;height:123px" role="img" aria-label="Photo: Brivex Duolo riders crossing a grassy slope below rocky peaks"></div>
  <svg class="accent" style="left:0;top:443px" width="420" height="26" viewBox="0 0 420 26"><polygon points="0,0 420,0 0,22" fill="#ffffff"/></svg>
  <div class="footer">
    <span class="contact-item"><svg viewBox="0 0 10 10"><path d="M2 1h2l1 2.5-1.2 1a5 5 0 0 0 2.7 2.7l1-1.2L10 7v2a1 1 0 0 1-1 1A8 8 0 0 1 1 2a1 1 0 0 1 1-1z" fill="#fff"/></svg>+41 27 555 01 23</span>
    <span class="contact-item"><svg viewBox="0 0 10 10"><rect x=".5" y="2" width="9" height="6.5" fill="none" stroke="#fff"/><path d="M.5 2.5L5 6l4.5-3.5" fill="none" stroke="#fff"/></svg>contact@valo-t-rekka.ch</span>
    <span class="contact-item">www.valo-t-rekka.ch</span>
  </div>
</section>

</body>
</html>
```